Restaurant, Nightclub

It's a Restaurant come nightclub. Our sign Lumen is white letters with blue edging on a black back ground.

Industry/Entity Type

Restaurant

Contact Information for Business Card

Lumen Stevenage Ltd
42 Mill Lane
Stevenage Herts SG2 7PQ

```html
<!DOCTYPE html>
<html lang="en">
<head>
<meta charset="utf-8">
<title>Lumen Stevenage Ltd – Sign</title>
<link rel="stylesheet" href="https://fonts.googleapis.com/css2?family=Arimo:wght@400;700&display=swap">
<style>
  :root {
    --backdrop: #d9d6d2;
    --sign-black: #000000;
    --sign-blue: #2eb4e8;
    --text-white: #ffffff;
  }
  * { margin: 0; padding: 0; box-sizing: border-box; }
  html, body {
    width: 1200px;
    height: 675px;
    overflow: hidden;
    background: var(--backdrop);
  }
  .canvas {
    position: relative;
    width: 1200px;
    height: 675px;
  }
  .sign {
    position: absolute;
    left: 95px;
    top: 37px;
    width: 980px;
    height: 613px;
    background: var(--sign-black);
    font-family: "Arimo", Arial, sans-serif;
    color: var(--text-white);
  }
  .stripe {
    position: absolute;
    left: 82px;
    width: 466px;
    height: 32px;
    background: var(--sign-blue);
  }
  .stripe-1 { top: 31px; }
  .stripe-2 { top: 97px; }
  .stripe-3 { top: 163px; }
  .stripe-4 { top: 230px; }
  .name-panel {
    position: absolute;
    left: 82px;
    top: 295px;
    width: 466px;
    height: 318px;
    background: var(--sign-blue);
  }
  .name-panel__wordmark {
    position: absolute;
    left: 0;
    right: 0;
    top: 103px;
    text-align: center;
    font-size: 110px;
    font-weight: 700;
    line-height: 1;
    color: var(--text-white);
    letter-spacing: 2px;
  }
  .contact {
    position: absolute;
    left: 540px;
    width: 400px;
    text-align: center;
  }
  .contact__company {
    top: 252px;
    font-size: 32px;
    line-height: 37px;
    font-weight: 400;
  }
  .contact__address {
    top: 322px;
    font-size: 24px;
    line-height: 30px;
    font-style: normal;
  }
</style>
</head>
<body>
  <main class="canvas">
    <section class="sign">
      <div class="stripe stripe-1"></div>
      <div class="stripe stripe-2"></div>
      <div class="stripe stripe-3"></div>
      <div class="stripe stripe-4"></div>
      <div class="name-panel">
        <div class="name-panel__wordmark">Lumen</div>
      </div>
      <h1 class="contact contact__company">Lumen Stevenage Ltd</h1>
      <address class="contact contact__address">
        42 Mill Lane<br>
        Stevenage Herts SG2 7PQ
      </address>
    </section>
  </main>
</body>
</html>
```